LinkedIn Banner Design for Asphalt & Parking Lot Company (Pavebright Dynamics LLC)

I need a professional LinkedIn banner designed for my company, Pavebright Dynamics LLC, based in Seattle. This banner should act as a visual “landing page header” for my profile and clearly communicate what we do within seconds.

The goal is to attract property managers, business owners, and commercial clients who are responsible for maintaining parking lots.

About the Business:
Pavebright Dynamics LLC provides asphalt parking lot services including:

Sealcoating
Crack sealing
Line striping
Asphalt maintenance & repair

Website: https://pavebrightdynamics.net
Location: Seattle, WA

Target Audience:

Property managers
Commercial real estate owners
Facility managers
Business owners with parking lots

Main Goal of the Banner:

Instantly show what we do
Build trust and professionalism
Generate leads from profile visitors
Make people think: “This is who I call for parking lot maintenance”

Headline / Tagline (Use This or Improve It):
Helping Property Managers Protect & Maintain Their Parking Lots

Subtext (optional but recommended):
Sealcoating • Crack Sealing • Line Striping

Design Style:

Clean, bold, and modern
Professional contractor/service look
High contrast and easy to read
Not cluttered

Branding / Colors:

Orange (primary accent color from logo)
Black / dark gray (asphalt tones)
White for contrast
Match branding from website and logo

Visual Direction (IMPORTANT):
Use high-quality, realistic images such as:

Freshly sealcoated, dark black parking lot
Clean, professionally striped parking lot
Before/after transformation (if done cleanly)

The banner should visually communicate:
“We make parking lots look new and last longer”

Focus more on RESULTS than workers.

Layout Notes:

Keep important text on the center/right side (profile photo covers left side)
Must look good on desktop and mobile
Avoid placing key elements on the far left

Optional Elements:

“Serving Seattle Area”
Website: pavebrightdynamics.net

Deliverables:

LinkedIn banner size: 1584 x 396 px
High-resolution file
Source file (PSD or AI)

What I DON’T Want:

Generic or low-quality stock designs
Overcrowded text
Cartoon-style construction graphics

Extra Notes:
This banner is important for lead generation. It should clearly communicate services even at a quick glance.

I’m open to creative ideas that align with attracting property managers and commercial clients.

Looking forward to your designs!

```html
<!DOCTYPE html>
<html lang="en">
<head>
<meta charset="utf-8">
<title>Pavebright Dynamics – LinkedIn Banner</title>
<link rel="stylesheet" href="https://fonts.googleapis.com/css2?family=Poppins:wght@500;600;700&display=swap">
<style>
  :root {
    --asphalt: #0d0d0d;
    --asphalt-light: #1c1c1c;
    --orange: #f7881f;
    --white: #ffffff;
    --grey: #cfcfcf;
    --photo-paving: #5d6a4a;
    --photo-striping: #3a3b3e;
    --photo-lot: #2b2e2c;
  }
  html, body {
    margin: 0;
    padding: 0;
    overflow: hidden;
    background: #ffffff;
  }
  .banner {
    position: relative;
    width: 1200px;
    height: 300px;
    overflow: hidden;
    background: radial-gradient(ellipse at 40% 40%, var(--asphalt-light), var(--asphalt) 75%);
    font-family: "Poppins", sans-serif;
    color: var(--white);
  }
  .photos {
    position: absolute;
    inset: 0;
  }
  .brand {
    position: absolute;
    left: 62px;
    top: 50px;
    display: flex;
    align-items: center;
    gap: 10px;
  }
  .brand-mark {
    width: 16px;
    height: 16px;
    background: var(--orange);
    flex: none;
  }
  .brand-name {
    width: 130px;
    font-size: 22px;
    font-weight: 700;
    color: var(--white);
    line-height: 26px;
  }
  .headline {
    position: absolute;
    left: 275px;
    top: 36px;
    margin: 0;
    font-size: 35px;
    font-weight: 700;
    line-height: 43px;
    text-transform: uppercase;
    letter-spacing: 0.4px;
    white-space: nowrap;
  }
  .headline .accent { color: var(--orange); }
  .services {
    position: absolute;
    left: 264px;
    top: 176px;
    width: 592px;
    height: 42px;
  }
  .services-band { position: absolute; inset: 0; }
  .service-list {
    position: absolute;
    left: 33px;
    top: 0;
    height: 42px;
    display: flex;
    align-items: center;
    gap: 22px;
    margin: 0;
    padding: 0;
    list-style: none;
  }
  .service {
    display: flex;
    align-items: center;
    gap: 9px;
    font-size: 15.5px;
    font-weight: 700;
    text-transform: uppercase;
    white-space: nowrap;
  }
  .service-icon { flex: none; display: block; }
  .contact {
    position: absolute;
    left: 295px;
    top: 240px;
    display: flex;
    gap: 42px;
    font-size: 17px;
    font-weight: 500;
  }
  .contact-item {
    display: flex;
    align-items: center;
    gap: 9px;
    white-space: nowrap;
  }
  .avatar-slot {
    position: absolute;
    left: 46px;
    top: 210px;
    width: 196px;
    height: 196px;
    border-radius: 50%;
    background: var(--grey);
    border: 5px solid var(--white);
    box-sizing: border-box;
  }
  .avatar-slot::after {
    content: "";
    position: absolute;
    left: 59px;
    top: 53px;
    width: 68px;
    height: 68px;
    border-radius: 50%;
    background: #f2f2f2;
  }
</style>
</head>
<body>
<div class="banner">

  <svg class="photos" width="1200" height="300" viewBox="0 0 1200 300">
    <polygon role="img" aria-label="Worker spreading fresh asphalt with a shovel" points="928,0 1114,0 1057,155 867,155" fill="var(--photo-paving)"/>
    <polygon role="img" aria-label="Striping machine painting a yellow line on fresh asphalt" points="864,163 1038,163 989,300 803,300" fill="var(--photo-striping)"/>
    <polygon role="img" aria-label="Freshly sealcoated and striped parking lot" points="1095,38 1200,38 1200,280 1004,280" fill="var(--photo-lot)"/>
  </svg>

  <div class="brand">
    <span class="brand-mark"></span>
    <span class="brand-name">Pavebright Dynamics</span>
  </div>

  <h1 class="headline">
    <span class="accent">Helping Property</span><br>
    Managers Protect &amp;<br>
    Maintain Their Parking Lots
  </h1>

  <div class="services">
    <svg class="services-band" width="592" height="42" viewBox="0 0 592 42">
      <polygon points="0,21 22,0 592,0 578,42 22,42" fill="var(--orange)"/>
    </svg>
    <ul class="service-list">
      <li class="service">
        <svg class="service-icon" width="16" height="22" viewBox="0 0 16 22"><path d="M6 1h4l5 17H1z" fill="#fff"/><rect x="0" y="18" width="16" height="3" fill="#fff"/><rect x="4" y="7" width="8" height="3" fill="var(--orange)"/><rect x="3" y="12" width="10" height="3" fill="var(--orange)"/></svg>
        Sealcoating
      </li>
      <li class="service">
        <svg class="service-icon" width="16" height="22" viewBox="0 0 16 22"><path d="M6 1h4l5 17H1z" fill="#fff"/><rect x="0" y="18" width="16" height="3" fill="#fff"/><rect x="4" y="7" width="8" height="3" fill="var(--orange)"/><rect x="3" y="12" width="10" height="3" fill="var(--orange)"/></svg>
        Crack Sealing
      </li>
      <li class="service">
        <svg class="service-icon" width="16" height="22" viewBox="0 0 16 22"><path d="M6 1h4l5 17H1z" fill="#fff"/><rect x="0" y="18" width="16" height="3" fill="#fff"/><rect x="4" y="7" width="8" height="3" fill="var(--orange)"/><rect x="3" y="12" width="10" height="3" fill="var(--orange)"/></svg>
        Line Striping
      </li>
    </ul>
  </div>

  <div class="contact">
    <span class="contact-item">
      <svg width="20" height="20" viewBox="0 0 20 20" fill="none"><circle cx="10" cy="10" r="9" fill="var(--orange)"/><ellipse cx="10" cy="10" rx="3.5" ry="8.5" stroke="var(--asphalt)" stroke-width="1.4"/><line x1="1.5" y1="10" x2="18.5" y2="10" stroke="var(--asphalt)" stroke-width="1.4"/></svg>
      pavebrightdynamics.net
    </span>
    <span class="contact-item">
      <svg width="16" height="21" viewBox="0 0 16 21"><path d="M8 0C3.6 0 0 3.5 0 7.9 0 13.5 8 21 8 21s8-7.5 8-13.1C16 3.5 12.4 0 8 0z" fill="var(--orange)"/></svg>
      Seattle, WA
    </span>
  </div>

  <div class="avatar-slot"></div>
</div>
</body>
</html>
```